Business Advisory Firm Business Card

A clean, very upscale looking business card. Not crowded.

Please include logo (attached) and:

Daria K. Pellworth
Four Marlow Court
New York, NY 10023
tel: (917) 555-0143
fax: (646) 555-0172
email: dpellworth@quarrystoneconsultants.example
website: www.quarrystoneconsultants.example

Target Market(s)

Business clients. Often real estate development firms, other advisory firms or growing companies that need assistance. I would like a card that looks impressive and confident.

Industry/Entity Type

Business

Colors

Designer to choose colors to be used in the design.

Requirements
Must have
• Impressive and confident. Please include logo.
Should not have
• nothing flashy...

```html
<!DOCTYPE html>
<html lang="en">
<head>
<meta charset="utf-8">
<title>Quarrystone Advisory Services – Business Card</title>
<link href="https://fonts.googleapis.com/css2?family=Montserrat:wght@600&family=Questrial&display=swap" rel="stylesheet">
<style>
  :root {
    --paper: #ffffff;
    --frame: #4a4a4a;
    --edge: #9a9a9a;
    --ink: #3a3a3a;
    --ink-soft: #4a4a4a;
    --accent: #9cc23c;
  }
  html, body {
    margin: 0;
    padding: 0;
    width: 1200px;
    height: 715px;
    overflow: hidden;
    background: var(--paper);
  }
  .card {
    position: relative;
    width: 1200px;
    height: 715px;
    box-sizing: border-box;
    border: 2px solid var(--edge);
    background: var(--paper);
  }
  .card__frame {
    position: absolute;
    left: 68px;
    top: 56px;
    width: 1060px;
    height: 592px;
    box-sizing: border-box;
    border: 2px solid var(--frame);
  }
  .holder-name {
    position: absolute;
    left: 133px;
    top: 162px;
    margin: 0;
    font-family: "Montserrat", sans-serif;
    font-weight: 600;
    font-size: 23px;
    letter-spacing: 3.4px;
    text-transform: uppercase;
    color: var(--ink);
  }
  .brand {
    position: absolute;
    left: 640px;
    top: 120px;
    display: flex;
    align-items: center;
    gap: 44px;
  }
  .brand__mark {
    width: 120px;
    height: 120px;
    background: var(--accent);
    flex: none;
  }
  .brand__name {
    margin: 0;
    font-family: "Questrial", sans-serif;
    font-weight: 400;
    font-size: 38px;
    line-height: 40px;
    color: var(--ink);
  }
  .contact {
    position: absolute;
    left: 133px;
    margin: 0;
    font-family: "Questrial", sans-serif;
    font-size: 26px;
    line-height: 30px;
    letter-spacing: 1.6px;
    color: var(--ink-soft);
    font-style: normal;
  }
  .contact--address { top: 354px; }
  .contact--phones { top: 443px; }
  .contact--web { top: 537px; }
  .contact span { display: block; }
</style>
</head>
<body>
  <div class="card">
    <div class="card__frame"></div>

    <h1 class="holder-name">Daria K. Pellworth</h1>

    <div class="brand">
      <div class="brand__mark" aria-hidden="true"></div>
      <p class="brand__name">Quarrystone<br>Advisory<br>Services, Inc.</p>
    </div>

    <address class="contact contact--address">
      <span>Four Marlow Court</span>
      <span>New York, NY 10023</span>
    </address>

    <p class="contact contact--phones">
      <span>t: (917) 555-0143</span>
      <span>f: (646) 555-0172</span>
    </p>

    <p class="contact contact--web">
      <span>e: dpellworth@quarrystoneconsultants.example</span>
      <span>W: www.quarrystoneconsultants.example</span>
    </p>
  </div>
</body>
</html>
```